Football field themed poster-game

I'm looking for a 22" x 29" size poster with a minimum of 300dpi, max of 300mb. File format can be jpg, gif, tiff or bmp. Would like the field portion of the poster to appear like a real grass football field. The field will need makers for each yard. I've added an addition simple clip art that shows another way for yard lines as well.The rest of the layout I would like similar, but made to look more professional. Wording should be the same as in the given draft and located in the same area or close to that area on the poster. The style is open, but should be a little minimalist in nature. Design work has to be original and cannot be taken from trademarked or copyrighted items.
Updates

Project Deadline Extended
Reason: I have 2 or 3 designs that really standout, but I would like to see just a few more.

Target Market(s)

Football fans

Font styles to use
Sans Serif

Colors

Designer to choose colors to be used in the design.

Requirements
Must have
• The design must have the same similar layout as the file I have submitted with the contest. The football field needs to be made to look like a real field with turf. boarders would be nice and a modern look.
Should not have
• hard to read fonts, changes to the major overall layout of poster.

```html
<!DOCTYPE html>
<html lang="en">
<head>
<meta charset="utf-8">
<title>Keg Bowl – Football Field Game Board</title>
<link rel="stylesheet" href="https://fonts.googleapis.com/css2?family=Russo+One&display=swap">
<style>
  :root{
    --canvas:#ffffff;
    --red:#e8141b;
    --red-deep:#c80d12;
    --blue:#1d9be3;
    --blue-deep:#0b74c4;
    --turf:#3e9a26;
    --turf-light:#58b532;
    --turf-dark:#2a7418;
    --yard-yellow:#f5d90a;
    --number:#f7d417;
    --line:#ffffff;
    --banner:#ffe21a;
    --navy:#1d2a8c;
    --gold:#d9a437;
    --gold-dark:#a8731e;
    --gold-light:#f6d98a;
  }
  *{box-sizing:border-box;margin:0;padding:0}
  html,body{width:910px;height:1200px;overflow:hidden;background:var(--canvas)}
  body{position:relative;font-family:"Russo One",sans-serif}

  /* ---------- Score board (left) ---------- */
  .score-board{position:absolute;left:19px;top:19px;width:311px;height:1163px;overflow:hidden;
    background:linear-gradient(180deg,var(--blue) 0%,var(--blue-deep) 100%)}
  .score-board__home-half{position:absolute;inset:0;
    background:radial-gradient(circle at 50% 55%,#ff3a2e 0%,var(--red) 45%,var(--red-deep) 100%);
    clip-path:polygon(0 0,100% 0,100% 548px,0 622px)}
  .score-board__visitor-half{position:absolute;inset:0;
    background:radial-gradient(circle at 50% 45%,#3fb6f2 0%,var(--blue) 50%,var(--blue-deep) 100%);
    clip-path:polygon(0 622px,100% 548px,100% 100%,0 100%)}
  .score-seal{position:absolute;left:44px;width:224px;height:224px}
  .score-seal--home{top:24px}
  .score-seal--visitor{top:902px}
  .score-label{position:absolute;left:0;width:100%;text-align:center;color:var(--line);
    font-size:30px;line-height:36px;letter-spacing:1px;font-style:italic}
  .score-label--home{top:276px;transform:rotate(180deg)}
  .score-label--visitor{top:846px}
  .game-title{position:absolute;left:155px;top:600px;transform:translate(-50%,-50%) rotate(90deg);
    color:var(--line);font-size:80px;line-height:.95;text-align:left;white-space:nowrap;letter-spacing:3px}
  .game-title__line{display:block}

  /* ---------- Playing field (right) ---------- */
  .field{position:absolute;left:348px;top:15px;width:543px;height:1167px;overflow:hidden}
  .end-zone{position:absolute;left:0;width:100%;height:116px}
  .end-zone--home{top:0;background:linear-gradient(180deg,var(--red-deep),var(--red))}
  .end-zone--visitor{bottom:0;height:117px;background:linear-gradient(180deg,var(--blue),var(--blue-deep))}
  .end-zone__crowd{position:absolute;left:0;top:0;width:100%;height:60px;opacity:.35}
  .end-zone--home .end-zone__crowd{background:linear-gradient(180deg,#a80a0e,transparent)}
  .end-zone--visitor .end-zone__crowd{background:linear-gradient(180deg,#0a5ea8,transparent)}
  .team-banner{position:absolute;left:114px;width:309px;height:38px}
  .end-zone--home .team-banner{top:44px}
  .end-zone--visitor .team-banner{top:25px}
  .team-banner__name{position:absolute;inset:0;display:flex;align-items:center;justify-content:center;
    color:var(--navy);font-size:27px;font-style:italic;letter-spacing:1px}
  .end-zone--home .team-banner__name{transform:rotate(180deg)}

  .turf{position:absolute;left:0;top:116px;width:100%;height:934px;overflow:hidden}
  .turf__grass{position:absolute;inset:0;width:100%;height:100%}
  .turf__yard-lines{position:absolute;inset:0;
    background:repeating-linear-gradient(180deg,transparent 0 92.4px,var(--yard-yellow) 92.4px 93.4px)}
  .turf__five-line{position:absolute;top:45.7px;height:934px;width:174px;
    background:repeating-linear-gradient(180deg,var(--line) 0 2px,transparent 2px 93.4px)}
  .turf__five-line--left{left:22px}
  .turf__five-line--right{left:341px}
  .turf__hash{position:absolute;top:0;height:934px;width:81px;
    background:repeating-linear-gradient(180deg,transparent 0 7.6px,rgba(255,255,255,.92) 7.6px 9.34px)}
  .turf__hash--left{left:69px}
  .turf__hash--right{left:389px}
  .yard-number{position:absolute;left:272px;
    color:var(--number);font-size:38px;font-style:italic;letter-spacing:1px;line-height:1;
    text-shadow:0 0 6px rgba(20,60,10,.6)}
  .yard-number--home-side{transform:translate(-50%,-50%) rotate(180deg)}
  .yard-number--visitor-side{transform:translate(-50%,-50%)}
</style>
</head>
<body>

<section class="score-board">
  <div class="score-board__home-half"></div>
  <div class="score-board__visitor-half"></div>

  <svg class="score-seal score-seal--home" viewBox="0 0 224 224" aria-hidden="true">
    <circle cx="112" cy="112" r="110" fill="var(--gold-dark)"/>
    <circle cx="112" cy="112" r="104" fill="var(--gold)"/>
    <circle cx="112" cy="112" r="96" fill="var(--gold-light)"/>
    <circle cx="112" cy="112" r="89" fill="#ffffff"/>
  </svg>
  <div class="score-label score-label--home">SCORE</div>

  <div class="game-title">
    <span class="game-title__line">KEG</span>
    <span class="game-title__line">BOWL</span>
  </div>

  <div class="score-label score-label--visitor">SCORE</div>
  <svg class="score-seal score-seal--visitor" viewBox="0 0 224 224" aria-hidden="true">
    <circle cx="112" cy="112" r="110" fill="var(--gold-dark)"/>
    <circle cx="112" cy="112" r="104" fill="var(--gold)"/>
    <circle cx="112" cy="112" r="96" fill="var(--gold-light)"/>
    <circle cx="112" cy="112" r="89" fill="#ffffff"/>
  </svg>
</section>

<section class="field">
  <div class="end-zone end-zone--home">
    <div class="end-zone__crowd" role="img" aria-label="Cheering crowd silhouettes"></div>
    <div class="team-banner">
      <svg width="309" height="38" viewBox="0 0 309 38" aria-hidden="true">
        <polygon points="30,0 279,0 279,38 30,38" fill="var(--banner)"/>
        <polygon points="0,0 12,0 26,19 12,38 0,38 14,19" fill="var(--banner)"/>
        <polygon points="14,0 22,0 36,19 22,38 14,38 28,19" fill="var(--red-deep)"/>
        <polygon points="309,0 297,0 283,19 297,38 309,38 295,19" fill="var(--banner)"/>
        <polygon points="295,0 287,0 273,19 287,38 295,38 281,19" fill="var(--red-deep)"/>
      </svg>
      <span class="team-banner__name">HOME</span>
    </div>
  </div>

  <div class="turf" role="img" aria-label="Grass turf football field">
    <svg class="turf__grass" viewBox="0 0 543 934" preserveAspectRatio="none" aria-hidden="true">
      <defs>
        <radialGradient id="turf-glow" cx="50%" cy="50%" r="70%">
          <stop offset="0" stop-color="var(--turf-light)"/>
          <stop offset=".6" stop-color="var(--turf)"/>
          <stop offset="1" stop-color="var(--turf-dark)"/>
        </radialGradient>
        <filter id="grass-dark" x="0" y="0" width="100%" height="100%">
          <feTurbulence type="fractalNoise" baseFrequency="0.9 0.45" numOctaves="3" seed="4"/>
          <feColorMatrix values="0 0 0 0 0.08  0 0 0 0 0.28  0 0 0 0 0.04  2.2 0 0 0 -0.95"/>
        </filter>
        <filter id="grass-light" x="0" y="0" width="100%" height="100%">
          <feTurbulence type="fractalNoise" baseFrequency="1.1 0.6" numOctaves="2" seed="11"/>
          <feColorMatrix values="0 0 0 0 0.55  0 0 0 0 0.85  0 0 0 0 0.3  0 2.2 0 0 -1.15"/>
        </filter>
      </defs>
      <rect width="543" height="934" fill="url(#turf-glow)"/>
      <rect width="543" height="934" filter="url(#grass-dark)"/>
      <rect width="543" height="934" filter="url(#grass-light)"/>
    </svg>
    <div class="turf__yard-lines"></div>
    <div class="turf__hash turf__hash--left"></div>
    <div class="turf__hash turf__hash--right"></div>
    <div class="turf__five-line turf__five-line--left"></div>
    <div class="turf__five-line turf__five-line--right"></div>
    <span class="yard-number yard-number--home-side" style="top:93.4px">10</span>
    <span class="yard-number yard-number--home-side" style="top:186.8px">20</span>
    <span class="yard-number yard-number--home-side" style="top:280.2px">30</span>
    <span class="yard-number yard-number--home-side" style="top:373.6px">40</span>
    <span class="yard-number yard-number--home-side" style="top:467px">50</span>
    <span class="yard-number yard-number--visitor-side" style="top:560.4px">40</span>
    <span class="yard-number yard-number--visitor-side" style="top:653.8px">30</span>
    <span class="yard-number yard-number--visitor-side" style="top:747.2px">20</span>
    <span class="yard-number yard-number--visitor-side" style="top:840.6px">10</span>
  </div>

  <div class="end-zone end-zone--visitor">
    <div class="end-zone__crowd" role="img" aria-label="Cheering crowd silhouettes"></div>
    <div class="team-banner">
      <svg width="309" height="38" viewBox="0 0 309 38" aria-hidden="true">
        <polygon points="30,0 279,0 279,38 30,38" fill="var(--banner)"/>
        <polygon points="0,0 12,0 26,19 12,38 0,38 14,19" fill="var(--banner)"/>
        <polygon points="14,0 22,0 36,19 22,38 14,38 28,19" fill="var(--navy)"/>
        <polygon points="309,0 297,0 283,19 297,38 309,38 295,19" fill="var(--banner)"/>
        <polygon points="295,0 287,0 273,19 287,38 295,38 281,19" fill="var(--navy)"/>
      </svg>
      <span class="team-banner__name">VISITORS</span>
    </div>
  </div>
</section>

</body>
</html>
```